Dovenmarch Luxury Landscapes

A landscape business card.

Target Market(s)

Middle aged and up. Professionals.

Industry/Entity Type

Landscape

Contact Information for Business Card

Thornbeck

Colors
0054AA
0677BA
7BADD7
CADEEF
E8F1F8
0094D4
00A9DD
6FCCEA
C7EBF8
E9F6FB

Requirements
Must have
• The color blue and silver be very attractive
Nice to have
• An embossed logo. A watermark of a plant or something that indicates that we are a landscape company in the background of the backside where list of services are offered. . List of services on the back.
Should not have
• Red, yellow, orange.

```html
<!DOCTYPE html>
<html lang="en">
<head>
<meta charset="utf-8">
<title>Dovenmarch Luxury Landscapes – Business Card</title>
<link href="https://fonts.googleapis.com/css2?family=Lato:wght@400;700&display=swap" rel="stylesheet">
<style>
  :root {
    --backdrop: #1d1d1e;
    --card: #4a494b;
    --card-light: #525153;
    --edge-blue: #1f3fd8;
    --deboss: #363537;
    --silver: #f2f2f2;
    --silver-soft: #dcdcdc;
  }
  * { margin: 0; padding: 0; box-sizing: border-box; }
  html, body {
    width: 1200px;
    height: 825px;
    overflow: hidden;
    background: var(--backdrop);
    font-family: "Lato", sans-serif;
  }
  .stage {
    position: relative;
    width: 1200px;
    height: 825px;
  }
  .card {
    position: absolute;
    width: 520px;
    height: 300px;
    border-radius: 22px;
    background: linear-gradient(135deg, var(--card-light), var(--card));
    box-shadow: 0 5px 0 var(--edge-blue), 0 18px 30px rgba(0,0,0,0.45);
  }
  .card--front { left: 70px; top: 110px; }
  .card--back  { left: 610px; top: 405px; }

  /* Front: debossed wordmark */
  .front-mark {
    position: absolute;
    inset: 0;
    display: flex;
    flex-direction: column;
    align-items: center;
    justify-content: center;
    color: var(--deboss);
    font-weight: 700;
    text-transform: uppercase;
    text-align: center;
  }
  .front-mark__name {
    font-size: 40px;
    letter-spacing: 3px;
    line-height: 1;
  }
  .front-mark__tagline {
    font-size: 17px;
    letter-spacing: 3px;
    margin-top: 6px;
  }

  /* Back: brand + contact */
  .back-brand {
    position: absolute;
    left: 34px;
    top: 0;
    bottom: 0;
    width: 180px;
    display: flex;
    flex-direction: column;
    justify-content: center;
    align-items: center;
    color: var(--silver);
    font-weight: 400;
    text-transform: uppercase;
    text-align: center;
  }
  .back-brand__name {
    font-size: 22px;
    letter-spacing: 2px;
    line-height: 1;
  }
  .back-brand__tagline {
    font-size: 9.5px;
    letter-spacing: 2px;
    margin-top: 5px;
  }
  .divider {
    position: absolute;
    left: 232px;
    top: 70px;
    height: 160px;
    width: 1.5px;
    background: var(--silver-soft);
  }
  .contact {
    position: absolute;
    left: 262px;
    top: 78px;
    color: var(--silver-soft);
    font-size: 13.5px;
    line-height: 1.45;
  }
  .contact__name {
    color: var(--silver);
    font-weight: 700;
    font-size: 24px;
    text-transform: uppercase;
    letter-spacing: 0.5px;
    margin-bottom: 8px;
  }
  .contact__block + .contact__block { margin-top: 6px; }
</style>
</head>
<body>
  <main class="stage">
    <section class="card card--front" aria-label="Business card front">
      <div class="front-mark">
        <span class="front-mark__name">Dovenmarch</span>
        <span class="front-mark__tagline">Luxury Landscapes</span>
      </div>
    </section>

    <section class="card card--back" aria-label="Business card back">
      <div class="back-brand">
        <span class="back-brand__name">Dovenmarch</span>
        <span class="back-brand__tagline">Luxury Landscapes</span>
      </div>
      <div class="divider"></div>
      <div class="contact">
        <p class="contact__name">Mara Ellison</p>
        <div class="contact__block">
          <p>18B Fernhollow Road, Thornbeck</p>
          <p>Nova Scotia, B4K 2T9</p>
        </div>
        <div class="contact__block">
          <p>902-555-GROW</p>
          <p>Dovenmarch.com</p>
        </div>
      </div>
    </section>
  </main>
</body>
</html>
```